Postcard Design

www.lirvo.com.au
i am an occupational therapist and professionally trained coach. i work with children, parents and disability service providers to achieve brilliant outcomes for children with special needs.
http://www.lirvo.com.au/service/for-families
I need a postcard to give parents to promote our family service coaching service
A family service coach will work with you to set specific goals for your child, build a dream team, design and manage your child's highly effective therapy and educational team to ensure brilliant outcomes for your child..
KORLU - you have done my business card previously. they were great thank you.

```html
<!DOCTYPE html>
<html lang="en">
<head>
<meta charset="utf-8">
<title>lirvo – Family Service Coaching Postcard</title>
<link rel="stylesheet" href="https://fonts.googleapis.com/css2?family=Arimo:wght@400;700&family=Roboto+Condensed:wght@700&display=swap">
<style>
  :root {
    --backdrop: #f2f2f2;
    --card-white: #ffffff;
    --brand-blue: #4d75b5;
    --deep-blue: #2f5fa6;
    --navy: #22388a;
    --swoosh: #7f9fd0;
    --badge-navy: #1f3a7a;
    --contact-blue: #3f66a8;
    --text-white: #ffffff;
  }
  * { box-sizing: border-box; margin: 0; padding: 0; }
  html, body {
    width: 1200px; height: 975px; overflow: hidden;
    background: var(--backdrop);
    font-family: "Arimo", Arial, sans-serif;
  }
  .postcard {
    position: absolute; left: 79px; top: 86px;
    width: 1042px; height: 802px;
    background: var(--card-white);
    overflow: hidden;
  }
  .family-photo {
    position: absolute; left: 340px; top: 0;
    width: 702px; height: 520px;
    background: linear-gradient(100deg,
      #e4e9e1 0%, #c9a98a 22%, #d8c4ae 40%, #8fa3bf 55%,
      #f0ebe4 68%, #c7b39f 80%, #6f8fbd 100%);
    -webkit-mask-image: linear-gradient(to right, transparent 0%, #000 20%);
            mask-image: linear-gradient(to right, transparent 0%, #000 20%);
  }
  .waves { position: absolute; left: 0; top: 0; width: 1042px; height: 802px; }
  .brand {
    position: absolute; left: 48px; top: 40px;
    display: flex; align-items: center; gap: 16px;
  }
  .brand-dot {
    width: 50px; height: 50px; border-radius: 50%;
    background: var(--brand-blue);
  }
  .brand-name {
    font-weight: 700; font-size: 44px; color: var(--brand-blue);
  }
  .headline {
    position: absolute; left: 52px; top: 154px;
    color: var(--brand-blue); line-height: 1;
  }
  .headline-line { display: block; font-size: 56px; font-weight: 400; margin-bottom: 10px; }
  .headline-strong { display: block; font-size: 58px; font-weight: 700; margin-top: 2px; letter-spacing: -0.5px; }
  .teamwork-photo {
    position: absolute; left: 53px; top: 374px;
    width: 297px; height: 297px; border-radius: 50%;
    border: 6px solid var(--card-white);
    background: linear-gradient(135deg, #9aa6b4 0%, #7d8a9b 45%, #56606e 100%);
  }
  .service-copy {
    position: absolute; left: 369px; top: 550px; width: 660px;
    color: var(--text-white); font-size: 20.5px; line-height: 29.5px;
  }
  .service-copy span { display: block; white-space: nowrap; }
  .contact-bar {
    position: absolute; left: 0; top: 694px;
    width: 1042px; height: 62px; background: var(--card-white);
    font-family: "Roboto Condensed", "Arial Narrow", sans-serif;
    font-weight: 700; font-size: 34px; color: var(--contact-blue);
  }
  .contact-item {
    position: absolute; top: 13px;
    display: flex; align-items: center; gap: 21px; line-height: 36px;
  }
  .contact-item.phone { left: 30px; }
  .contact-item.email { left: 309px; gap: 16px; }
  .contact-item.web { left: 703px; gap: 12px; }
  .contact-badge {
    width: 36px; height: 36px; border-radius: 6px;
    background: var(--badge-navy); color: var(--text-white);
    font-size: 26px; display: flex; align-items: center; justify-content: center;
  }
  .footer-band {
    position: absolute; left: 0; top: 756px; width: 1042px; height: 46px;
    background: linear-gradient(to right, #3466ab, #4f7dbd 50%, #3466ab);
  }
</style>
</head>
<body>
  <main class="postcard">
    <div class="family-photo" role="img" aria-label="Photo of a smiling family with two young children meeting a coach on a sofa"></div>

    <svg class="waves" viewBox="0 0 1042 802" aria-hidden="true">
      <defs>
        <linearGradient id="panelBlue" x1="0" y1="0" x2="1" y2="1">
          <stop offset="0" stop-color="#2f62a9"/>
          <stop offset="0.55" stop-color="#4b7bbb"/>
          <stop offset="1" stop-color="#3466ab"/>
        </linearGradient>
      </defs>
      <path d="M0,360 C200,420 380,520 560,515 C760,510 900,460 1042,400 L1042,802 L0,802 Z" fill="url(#panelBlue)"/>
      <path d="M0,350 C200,410 380,508 560,503 C760,498 900,448 1042,388 L1042,400 C900,460 760,510 560,515 C380,520 200,420 0,362 Z" fill="#22388a"/>
      <path d="M600,505 C800,488 950,420 1042,300 L1042,388 C900,448 760,498 560,503 Z" fill="#7f9fd0"/>
    </svg>

    <div class="brand">
      <span class="brand-dot"></span>
      <span class="brand-name">lirvo</span>
    </div>

    <h1 class="headline">
      <span class="headline-line">FAMILY</span>
      <span class="headline-line">SERVICE</span>
      <span class="headline-strong">COACHING</span>
    </h1>

    <div class="teamwork-photo" role="img" aria-label="Photo of several hands joining coloured puzzle pieces"></div>

    <p class="service-copy">
      <span>A family service coach will work with you to set specific</span>
      <span>goals for your child, build a dream team, design and</span>
      <span>manage your child's highly effective therapy and educational</span>
      <span>team to ensure brilliant outcomes for your child..</span>
    </p>

    <div class="contact-bar">
      <div class="contact-item phone"><span class="contact-badge">P.</span><span>0412 555 708</span></div>
      <div class="contact-item email"><span class="contact-badge">E.</span><span>mara@lirvo.com.au</span></div>
      <div class="contact-item web"><span class="contact-badge">W.</span><span>www.lirvo.com.au</span></div>
    </div>

    <div class="footer-band"></div>
  </main>
</body>
</html>
```